Ridgeline Stick Works
Custom Wood Bats
guaranteed please...
For some reason, my numbers aren't showing up, but for the ones I rated, could you put the rest of the stationary with the cards? Looks great you all. Thanks!
increase the price please.....
#3, I like that. Can you make the seams red on the front of the ball or will the address not show up if you do?
Can you combine 7 & 8
Hi - so it is ok to alter the logo colors on the logo itself?
I would like to see some different colors. Maybe a navy blue print on the logo and then in the red part. Leave the ball white with red stitches. Look forward to seeing your interpretations.
Just uploaded it. My name doesn't have a "c" in it. Could you also put "Ridgeline Stick Works" somewhere on the front of the card? Also, I'm not a big fan of the all caps. Thanks for your design.
can you upload the original logo,please?

```html
<!DOCTYPE html>
<html lang="en">
<head>
<meta charset="utf-8">
<title>Ridgeline Stick Works – Stationery Set</title>
<link rel="stylesheet" href="https://fonts.googleapis.com/css2?family=Roboto:wght@400;700;900&display=swap">
<style>
  :root {
    --brand-red: #e31e26;
    --paper: #ffffff;
    --backdrop: #ffffff;
    --edge: #d9d9d9;
    --shadow: rgba(0,0,0,0.22);
  }
  * { box-sizing: border-box; margin: 0; padding: 0; }
  html, body { width: 1200px; height: 681px; overflow: hidden; background: var(--backdrop); }
  body { position: relative; font-family: "Roboto", Arial, sans-serif; color: var(--brand-red); }

  .sheet {
    position: absolute;
    background: var(--paper);
    border: 1px solid var(--edge);
    box-shadow: 4px 5px 10px var(--shadow);
    overflow: hidden;
  }
  .swoosh { position: absolute; left: 0; top: 0; width: 100%; display: block; }

  .wordmark {
    position: absolute;
    font-weight: 900;
    color: var(--brand-red);
    line-height: 1.05;
    letter-spacing: -0.2px;
  }
  .small-print { position: absolute; font-size: 7px; line-height: 1.45; color: var(--brand-red); font-weight: 700; }

  /* envelope front */
  .envelope-front { left: 19px; top: 91px; width: 461px; height: 161px; }
  .envelope-front .wordmark { left: 26px; top: 68px; font-size: 15px; width: 110px; }
  .envelope-front .small-print { left: 26px; top: 108px; }

  /* envelope back */
  .envelope-back { left: 19px; top: 312px; width: 461px; height: 168px; }
  .envelope-back .flap { position: absolute; left: 0; top: 0; width: 100%; height: 70px; display: block; }
  .ball-disc {
    position: absolute; border-radius: 50%; background: var(--paper);
  }
  .envelope-back .ball-disc { left: 214px; top: 20px; width: 34px; height: 34px; }

  /* letterhead */
  .letterhead { left: 619px; top: 43px; width: 324px; height: 586px; }
  .letterhead .wordmark { left: 22px; top: 76px; font-size: 17px; width: 130px; }
  .letterhead .small-print { left: 22px; top: 128px; }

  /* business card front */
  .card-front { left: 972px; top: 163px; width: 175px; height: 108px; }
  .card-front .wordmark { left: 10px; top: 34px; font-size: 11px; width: 70px; }
  .card-front .card-name { position: absolute; left: 92px; top: 28px; font-size: 7px; font-weight: 700; line-height: 1.35; }
  .card-front .small-print { left: 92px; top: 54px; font-size: 5px; }

  /* business card back */
  .card-back { left: 972px; top: 300px; width: 175px; height: 108px; background: var(--brand-red); border-color: var(--brand-red); }
  .card-back .ball-disc { left: 70px; top: 24px; width: 34px; height: 34px; }
  .card-back .web { position: absolute; left: 60px; top: 82px; font-size: 6px; font-weight: 700; color: var(--paper); }
</style>
</head>
<body>

  <!-- Envelope front -->
  <section class="sheet envelope-front" aria-label="Envelope front">
    <svg class="swoosh" viewBox="0 0 461 60" height="60" preserveAspectRatio="none">
      <path d="M0 28 C120 0 320 -2 461 14 L461 0 L0 0 Z" fill="var(--brand-red)"/>
      <path d="M0 46 C140 12 330 8 461 22 L461 17 C320 4 130 8 0 36 Z" fill="var(--brand-red)"/>
      <path d="M30 50 C160 22 340 20 461 30 L461 28 C340 16 160 18 30 50 Z" fill="var(--brand-red)"/>
    </svg>
    <div class="wordmark">Ridgeline Stick Works</div>
    <div class="small-print">P.O. Box 418, Alder Falls, NC 28120</div>
  </section>

  <!-- Envelope back -->
  <section class="sheet envelope-back" aria-label="Envelope back">
    <svg class="flap" viewBox="0 0 461 70" preserveAspectRatio="none">
      <path d="M0 0 H461 V56 L440 70 H21 L0 56 Z" fill="var(--brand-red)"/>
    </svg>
    <div class="ball-disc"></div>
  </section>

  <!-- Letterhead -->
  <section class="sheet letterhead" aria-label="Letterhead">
    <svg class="swoosh" viewBox="0 0 324 70" height="70" preserveAspectRatio="none">
      <path d="M0 36 C90 4 230 -2 324 16 L324 0 L0 0 Z" fill="var(--brand-red)"/>
      <path d="M0 56 C100 16 240 10 324 26 L324 20 C230 4 90 10 0 44 Z" fill="var(--brand-red)"/>
      <path d="M24 62 C120 28 250 24 324 36 L324 33 C250 20 120 24 24 62 Z" fill="var(--brand-red)"/>
    </svg>
    <div class="wordmark">Ridgeline Stick Works</div>
    <div class="small-print">
      P.O. Box 418, Alder Falls, NC 28120<br>
      Phone: 704.555.0182 &bull; www.ridgelinestickworks.com
    </div>
  </section>

  <!-- Business card front -->
  <section class="sheet card-front" aria-label="Business card front">
    <svg class="swoosh" viewBox="0 0 175 24" height="24" preserveAspectRatio="none">
      <path d="M0 12 C50 0 120 0 175 6 L175 0 L0 0 Z" fill="var(--brand-red)"/>
      <path d="M0 20 C60 6 130 4 175 10 L175 8 C120 2 50 4 0 16 Z" fill="var(--brand-red)"/>
    </svg>
    <div class="wordmark">Ridgeline Stick Works</div>
    <div class="card-name">Jordan Hale<br>Owner</div>
    <div class="small-print">
      P.O. Box 418<br>Alder Falls, NC 28120<br>Phone: 704.555.0182<br>hello@ridgelinestickworks.com
    </div>
  </section>

  <!-- Business card back -->
  <section class="sheet card-back" aria-label="Business card back">
    <div class="ball-disc"></div>
    <div class="web">www.ridgelinestickworks.com</div>
  </section>

</body>
</html>
```